Silver Heron Staffing Agency

I need to make a brochure/catalogue that represent our company, telling our clients what we do, our values, fields of industry that we taken care of, so they know who we are, what we did, and how we do it.
I do have a logo and simple brochure design before that i really need to upgrade (i will give it as an example on this attachment).

What I want in the new design is :
1. More pictures and little bit of explanation in each industry we work with.
2. Attractive design that make people LOOK at the brochure and not just throw it in the trash.
3. Still use the combination color of the company logo itself, which is Golden Brown.

```html
<!DOCTYPE html>
<html lang="en">
<head>
<meta charset="utf-8">
<title>Silver Heron Staffing Agency – Trifold Brochure</title>
<link href="https://fonts.googleapis.com/css2?family=Montserrat:wght@400;500;600;700;800&display=swap" rel="stylesheet">
<style>
  :root{
    --gold:#b0903c;
    --gold-dark:#8f7430;
    --gold-light:#d8bd7a;
    --ink:#1d1d1d;
    --text:#3a3a3a;
    --paper:#ffffff;
    --mist:#eeeeee;
    --backdrop:#e6e6e6;
  }
  *{box-sizing:border-box;margin:0;padding:0}
  html,body{width:800px;height:1200px;overflow:hidden}
  body{background:var(--backdrop);font-family:'Montserrat',sans-serif;color:var(--text);position:relative}
  .spread{position:absolute;left:30px;width:740px;height:528px;display:flex;background:var(--paper);box-shadow:0 4px 14px rgba(0,0,0,.18)}
  .spread--outside{top:40px}
  .spread--inside{top:620px}
  .panel{position:relative;width:246.67px;height:100%;overflow:hidden;display:flex;flex-direction:column}
  .heading{font-size:10px;font-weight:700;color:var(--gold);text-transform:uppercase;letter-spacing:.3px;margin-bottom:7px}
  .heading span{border-bottom:1.2px solid var(--gold)}
  .copy{font-size:6.1px;line-height:1.42;text-align:justify}
  .photo{background:linear-gradient(135deg,#c9a36a,#7a5a3a);}

  /* outside: panel 1 */
  .intro{height:118px;padding:16px 14px 0}
  .photo--housekeeper{height:240px;background:linear-gradient(120deg,#d9d4d0 0%,#b6bfd2 35%,#a4532f 70%,#6b2a18 100%)}
  .specialties{flex:1;padding:12px 14px}
  .specialties .heading{line-height:1.3;margin-bottom:10px}
  .specialty-list{display:flex;font-size:6.3px}
  .specialty-list ul{list-style:none}
  .specialty-list li{margin-bottom:7px;display:flex;align-items:center;gap:4px}
  .specialty-list li::before{content:"";width:4px;height:4px;border:.8px solid var(--gold)}
  .specialty-list .divider{width:1px;background:var(--ink);margin:0 14px 0 18px;height:42px}

  /* outside: panel 2 */
  .location{height:240px;background:var(--gold);padding:16px 14px;position:relative}
  .location .heading{color:var(--paper)}
  .location .heading span{border-color:var(--paper)}
  .map{position:absolute;left:22px;top:44px;width:110px;height:180px;background:linear-gradient(160deg,#f3ead5,#e2d1a6);border-radius:40% 20% 30% 10%/20% 30% 60% 40%}
  .state-labels{position:absolute;left:140px;top:72px;font-size:7px;font-weight:700;color:var(--paper);line-height:1.35}
  .state-lines{position:absolute;left:96px;top:70px}
  .contact{flex:1;padding:12px 14px}
  .brand-name{font-size:9px;font-weight:700;color:var(--gold);margin-bottom:10px}
  .contact-row{display:flex;align-items:flex-start;gap:5px;font-size:6.3px;margin-bottom:5px}
  .contact-row svg{flex:none;margin-top:1px}
  .phone{font-size:9px;font-weight:700;color:var(--ink)}

  /* outside: cover */
  .cover-art{position:absolute;inset:0}
  .cover-brand{position:absolute;top:38px;left:22px;font-size:13px;font-weight:700;color:var(--gold)}
  .cover-title{position:absolute;left:22px;top:392px;font-size:23px;font-weight:800;color:var(--ink);line-height:1.22;letter-spacing:.3px}
  .cover-title em{font-style:normal;color:var(--gold)}
  .web{position:absolute;left:22px;top:494px;font-size:7px;color:var(--ink);font-weight:600}

  /* inside */
  .panel--mist{background:var(--mist)}
  .block{padding:14px 14px 0}
  .about{height:195px}
  .culture{height:136px;background:var(--gold)}
  .culture .heading{color:var(--ink)}
  .culture .heading span{border-color:var(--ink)}
  .culture .copy{color:#f5ecd7}
  .mission{flex:1;position:relative;background:var(--paper)}
  .mission .copy p+p{margin-top:8px}
  .slogan{position:absolute;left:14px;bottom:12px;font-size:22px;font-weight:800;letter-spacing:.6px;color:var(--gold)}
  .panel--dark{background:var(--ink)}
  .panel--dark .copy{color:#d8d8d8}
  .process{height:195px}
  .process .heading+.copy{margin-bottom:10px}
  .photo--manager{height:136px;background:linear-gradient(100deg,#c4ccd8 0%,#8a6a48 45%,#b64a2a 75%,#5c3a24 100%)}
  .industries-served{flex:1;position:relative}
  .feature{display:flex;gap:8px}
  .feature h4,.item h4{font-size:8px;color:var(--ink);font-weight:700;margin-bottom:3px}
  .panel--dark .feature h4{color:var(--paper)}
  .photo--warehouse{flex:none;width:80px;height:90px;background:linear-gradient(150deg,#d3d7d9,#8a94a0 50%,#c9d24a 80%,#3c4450);outline:1px solid #fff}
  .slogan--light{color:var(--paper)}
  .items{height:463px;padding:14px 14px 0;display:flex;flex-direction:column;gap:6px}
  .item{height:110px;display:flex;gap:8px}
  .item .text{flex:1}
  .thumb{flex:none;width:86px;height:94px;outline:1px solid #ccc;outline-offset:1px}
  .thumb--hotel{background:linear-gradient(150deg,#a88d72,#e9e3dc 55%,#f6f3ef)}
  .thumb--farming{background:linear-gradient(140deg,#3c3430,#d9d2c8 55%,#a8453a)}
  .thumb--mail{background:linear-gradient(160deg,#f4f4f4,#2e6fb8 55%,#d49a5a)}
  .thumb--landfill{background:linear-gradient(150deg,#4f6a3a,#e5d23a 55%,#6b8a44)}
  .tagline{height:65px;background:var(--gold);color:var(--ink);font-size:21px;font-weight:800;text-align:center;line-height:1.02;padding-top:10px;letter-spacing:.4px}
</style>
</head>
<body>

<!-- Outside spread -->
<section class="spread spread--outside" aria-label="Brochure outside">
  <article class="panel">
    <div class="intro">
      <h2 class="heading"><span>Indus</span>tries</h2>
      <p class="copy">Need industry-leading talent for your organization? Career options that are ideal for your skills and experience? The professionals at Silver Heron Staffing have the tools and knowledge to help you make the perfect match.</p>
    </div>
    <div class="photo photo--housekeeper" role="img" aria-label="Smiling hotel housekeeper in a light blue uniform beside a service cart in a hotel corridor"></div>
    <div class="specialties">
      <h2 class="heading">Our specialties<br>include staffing<br>for the following<br>industries</h2>
      <div class="specialty-list">
        <ul><li>Warehousing</li><li>Hotel</li><li>Casino</li><li>Paper Mailing</li></ul>
        <div class="divider"></div>
        <ul><li>Transportation</li><li>Landfill</li><li>Food Handling</li></ul>
      </div>
    </div>
  </article>

  <article class="panel">
    <div class="intro">
      <h2 class="heading"><span>Conta</span>ct form</h2>
      <p class="copy" style="text-align:left">Thank you for choosing Silver Heron Staffing. If you have temporary jobs you are hiring for please get in touch with Northgate Enterprise Solution. We are able to help with all your staffing and employment needs.</p>
    </div>
    <div class="location">
      <h2 class="heading"><span>Our L</span>ocation</h2>
      <div class="map" role="img" aria-label="Outline map of the eastern United States"></div>
      <svg class="state-lines" width="44" height="60" viewBox="0 0 44 60" aria-hidden="true">
        <g stroke="#fff" stroke-width=".8" fill="none">
          <line x1="0" y1="12" x2="42" y2="6"/><line x1="2" y1="20" x2="42" y2="15"/>
          <line x1="4" y1="26" x2="42" y2="24"/><line x1="4" y1="30" x2="42" y2="33"/>
          <line x1="2" y1="34" x2="42" y2="42"/>
        </g>
      </svg>
      <div class="state-labels">New York<br>Pennsylvania<br>New Jersey<br>Delaware<br>Virginia</div>
    </div>
    <div class="contact">
      <div class="brand-name">Silver Heron Inc.</div>
      <h2 class="heading"><span>Conta</span>ct info</h2>
      <div class="contact-row">
        <svg width="8" height="8" viewBox="0 0 10 10" aria-hidden="true"><path d="M2 0.5l2 2.2-1 1.3c.7 1.5 1.6 2.4 3 3l1.3-1 2.2 2-1.3 1.6C4.6 9.3.7 5.4.4 1.8z" fill="var(--gold)"/></svg>
        <span class="phone">555-204-7781</span>
      </div>
      <div class="contact-row">
        <svg width="7" height="9" viewBox="0 0 8 11" aria-hidden="true"><path d="M4 0a4 4 0 0 1 4 4c0 3-4 7-4 7S0 7 0 4a4 4 0 0 1 4-4zm0 2.3a1.7 1.7 0 1 0 0 3.4 1.7 1.7 0 0 0 0-3.4z" fill="var(--gold)"/></svg>
        <span>42 Birch Lane, suite 300<br>Maple Ridge, NJ 08000</span>
      </div>
      <div class="contact-row">
        <svg width="8" height="6" viewBox="0 0 10 7" aria-hidden="true"><rect width="10" height="7" fill="var(--gold)"/><path d="M0 0l5 4 5-4" stroke="#fff" stroke-width=".9" fill="none"/></svg>
        <span>info@silverheronstaffing.com</span>
      </div>
      <div class="contact-row">
        <svg width="8" height="8" viewBox="0 0 10 10" aria-hidden="true"><g fill="none" stroke="var(--gold)" stroke-width="1"><circle cx="5" cy="5" r="4.4"/><ellipse cx="5" cy="5" rx="2" ry="4.4"/><line x1=".6" y1="5" x2="9.4" y2="5"/></g></svg>
        <span>www.silverheronstaffing.com</span>
      </div>
    </div>
  </article>

  <article class="panel">
    <svg class="cover-art" width="247" height="528" viewBox="0 0 247 528" aria-hidden="true">
      <polygon points="0,118 122,118 8,238 122,358 0,358" fill="var(--gold)"/>
      <polygon points="247,12 247,472 14,238" fill="var(--gold)"/>
    </svg>
    <div class="photo" role="img" aria-label="Businessman with a briefcase climbing a staircase toward a city skyline"
      style="position:absolute;inset:0;clip-path:polygon(100% 3.5%,100% 87.5%,9% 45%);background:linear-gradient(200deg,#e2a45e 0%,#9a8a7a 40%,#4d5a6c 75%,#2a3340 100%)"></div>
    <div class="cover-brand">Silver Heron Inc.</div>
    <h1 class="cover-title">YOUR<br>BEST WAY<br>TO <em>SUCCEED</em></h1>
    <div class="web">www.<b>silverheronstaffing</b>.com</div>
  </article>
</section>

<!-- Inside spread -->
<section class="spread spread--inside" aria-label="Brochure inside">
  <article class="panel panel--mist">
    <div class="block about">
      <h2 class="heading"><span>About</span> us</h2>
      <p class="copy">With more than 18 years of experience Silver Heron Staffing provided staffing services to a wide array of locations, all throughout Pennsylvania. Through the last few years we have expanded to 5 other states including New York, New Jersey, Delaware, Virginia and Georgia. Our ethics are a critical building block of our business. Our own success is based on adherence to the highest ethical standards, long-term client relationships, the ability to identify top candidates, and the high-quality professional development of Silver Heron Staffing professionals protecting the confidentiality and interests of clients and candidates.</p>
    </div>
    <div class="block culture">
      <h2 class="heading"><span>Cultu</span>re</h2>
      <p class="copy">Silver Heron Staffing believes in equal opportunity for all, regardless of gender, race, ethic, origin, religion, or handicap. The staffing policies and practices of Silver Heron Staffing for our organization, our clients and candidates are fully non-discriminatory. Our employees are our most valuable asset. We strive to create a work environment of professionalism, trust and respect that will continuously provide our staff with motivation, challenge, and professional growth to aim our most important goal; CLIENT SATISFACTION.</p>
    </div>
    <div class="block mission">
      <h2 class="heading"><span>Missi</span>on</h2>
      <div class="copy">
        <p>Silver Heron Staffing is more than a staffing company; we want to become your business partner. We understand that payroll and employee-service</p>
        <p>overhead can be one of the largest expenses for your business. Through our partnership-network programs Silver Heron Staffing can help you reduce the hard-costs of your business expenses. We take responsibility for all our placed employees, including payroll taxes and benefits allowing you to focus on running your business.</p>
      </div>
      <div class="slogan">CONNECTING</div>
    </div>
  </article>

  <article class="panel panel--dark">
    <div class="block process">
      <h2 class="heading"><span>Our p</span>rocess</h2>
      <p class="copy">Our screening process includes a thorough interview with each potential candidate to give us insight into the candidate's previous work history, skills, communication abilities and career goals as well as reference checks with their previous employers.</p>
      <h2 class="heading"><span>Our s</span>ervices</h2>
      <p class="copy">Silver Heron Staffing's personalized services, expertise and affordable rates are key factors of our success and being our client's choice staffing agency. Our contingent and contract-to-hire employees are looking for flexible careers in New York, New Jersey, Pennsylvania, Delaware, Virginia and Georgia.</p>
    </div>
    <div class="photo photo--manager" role="img" aria-label="Smiling manager with a clipboard standing in a warehouse full of boxes"></div>
    <div class="block industries-served">
      <h2 class="heading"><span>Indus</span>tries we serve:</h2>
      <div class="feature">
        <div>
          <h4>Warehousing</h4>
          <p class="copy">Warehousing is the act of storing goods that will be sold or distributed later. While a small, home-based business might be warehousing products in a spare room, basement, or garage, larger businesses typically own or rent space in a building that is specifically designed for storage.</p>
        </div>
        <div class="photo photo--warehouse" role="img" aria-label="Warehouse worker in a hard hat and safety vest holding a clipboard"></div>
      </div>
      <div class="slogan slogan--light">OPPORTUNITY</div>
    </div>
  </article>

  <article class="panel">
    <div class="items">
      <div class="item">
        <div class="text"><h4>Hotel</h4><p class="copy" style="text-align:left">Whether you are travelling for business or pleasure, the luxury hotel services offered by the five star Grand Harbor Hotel make it an ideal choice for your stay in Riga, Latvia.</p></div>
        <div class="thumb thumb--hotel" role="img" aria-label="Hotel attendant holding a stack of folded white towels"></div>
      </div>
      <div class="item">
        <div class="thumb thumb--farming" role="img" aria-label="Worker preparing food at a kitchen counter"></div>
        <div class="text"><h4>Farming</h4><p class="copy" style="text-align:left">Farming is growing crops or keeping animals by people for food and raw materials. Farming is a part of agriculture.</p></div>
      </div>
      <div class="item">
        <div class="text"><h4>Paper Mailling</h4><p class="copy" style="text-align:left">Our paper mailing courier sacks have become popular with businesses and organisations looking for sustainable alternatives to polythene mailing bags.</p></div>
        <div class="thumb thumb--mail" role="img" aria-label="Courier in a blue cap carrying a cardboard parcel and clipboard"></div>
      </div>
      <div class="item">
        <div class="thumb thumb--landfill" role="img" aria-label="Worker in a yellow protective suit and mask outdoors"></div>
        <div class="text"><h4>Landfill</h4><p class="copy" style="text-align:left">Landfill gas is produced by wet organic waste decomposing under anaerobic conditions in a landfill. ... landfills gas production is dependant, on the degradation status of the waste material as well as moisture and temperature, all of which may vary greatly in different parts of the landfill body.</p></div>
      </div>
    </div>
    <div class="tagline">WITH TODAY'S<br>TOP TALENT</div>
  </article>
</section>

</body>
</html>
```